Home page design for a live auction website.

Hi, we are looking at finding a good design for an auction website, only home page .. We will not be selling anything online, so the website will only be a portal where visitors can check about our company, upcoming auctions, online catalogues etc.
See attached our logo. Please use the same red that you see on the logo in the designs that you provide.
The final design should communicate high-end auction website, as we will be selling expensive piece of arts and antiques.
We should have a main frame where images of arts will circulate, with description of the art piece. just like on http://paris.vellmarotte-quisande.com/
(but with a better design overall) and of course a menu with different tabs, like "about us", "previous sales" "next sales", "contact" , "how to buy", "meet our specialists".

Target Market(s)

High end segment, who can afford to pay up to 250'000 for a piece of art

Industry/Entity Type

Online

Number of Pages Required

1 page

Requirements
Must have
• a frame with images rotating, just like on http://paris.vellmarotte-quisande.com/ . but the rest of the design should be more refined.
• we should also have a strong call to action, "Free online estimation", click here, estimation delivered in 48 hours"
Nice to have
• Tremaux Auctions, the brand should be well visible

```html
<!DOCTYPE html>
<html lang="en">
<head>
<meta charset="utf-8">
<title>Tremaux Auctions</title>
<link href="https://fonts.googleapis.com/css2?family=Open+Sans:wght@400;600;700;800&display=swap" rel="stylesheet">
<style>
:root{
  --red:#c8102e;
  --red-dark:#a50d25;
  --ink:#222;
  --text:#666;
  --muted:#999;
  --line:#e3e3e3;
  --light:#f1f1f1;
  --footer:#3a3d42;
  --footer-text:#b9bcc1;
  --white:#fff;
}
*{box-sizing:border-box;margin:0;padding:0}
html,body{width:1200px;height:2356px;overflow:hidden}
body{font-family:'Open Sans',Arial,sans-serif;color:var(--text);background:var(--white);font-size:14px}
a{color:inherit;text-decoration:none}

.site-header{height:88px;display:flex;align-items:center;justify-content:space-between;padding:0 80px}
.brand{display:flex;align-items:center;gap:12px;font-weight:700;font-size:22px;color:var(--red)}
.brand-mark{width:34px;height:34px;border-radius:50%;background:var(--red)}
.header-right{display:flex;align-items:center;gap:40px}
.contact-line{display:flex;align-items:center;gap:12px}
.phone-icon{width:38px;height:38px;border-radius:50%;border:2px solid var(--red);display:flex;align-items:center;justify-content:center}
.contact-line strong{display:block;font-size:20px;color:var(--ink);font-weight:700;line-height:1.1}
.contact-line span{font-size:12px;color:var(--muted)}
.btn{display:inline-block;background:var(--red);color:var(--white);font-weight:700;font-size:13px;text-transform:uppercase;padding:12px 30px}

.main-nav{height:32px;background:var(--red);display:flex;justify-content:space-between;align-items:center;padding:0 150px;color:var(--white);font-size:13px;font-weight:600}

.hero{position:relative;height:588px;background:radial-gradient(ellipse at 62% 40%,#9a9a9a 0%,#4a4a4a 35%,#141414 75%)}
.hero-photo{position:absolute;inset:0}
.hero-badge{position:absolute;left:100px;top:270px;width:300px;height:300px;border-radius:50%;background:var(--red);color:var(--white);display:flex;flex-direction:column;align-items:center;justify-content:center;text-align:center;box-shadow:0 0 0 10px rgba(200,16,46,.35)}
.hero-badge h1{font-size:24px;font-weight:800;line-height:1.25;text-transform:uppercase}
.hero-badge h1 .big{font-size:34px}
.hero-badge .shop{margin-top:18px;font-size:13px;font-weight:700}
.hero-badge .shop-arrow{margin-top:8px;width:30px;height:30px;border-radius:50%;background:var(--white)}
.hero-dots{position:absolute;bottom:24px;left:50%;transform:translateX(-50%);display:flex;gap:10px}
.hero-dots i{width:10px;height:10px;border-radius:50%;background:rgba(255,255,255,.5)}
.hero-dots i.on{background:var(--red)}

.welcome{display:flex;gap:60px;padding:40px 80px 0;height:392px}
.welcome-photo{width:520px;height:316px;background:linear-gradient(135deg,#6b4a2e,#c9a874 45%,#3a5a7a)}
.welcome-text{padding-top:20px}
.welcome-text h2{font-size:28px;font-weight:400;color:var(--ink);line-height:1.2}
.welcome-text h2 strong{display:block;font-size:40px;color:var(--red);font-weight:800;text-transform:uppercase}
.welcome-text p{margin:18px 0 26px;line-height:1.75;font-size:14px}

.on-sale{background:var(--light);height:400px;padding:30px 80px 0}
.section-head{position:relative;text-align:center;font-size:20px;font-weight:700;color:var(--ink);text-transform:uppercase}
.arrows{position:absolute;right:0;top:2px;display:flex;gap:8px}
.arrows i{width:26px;height:26px;border-radius:50%;background:#c4c4c4}
.lots{display:flex;justify-content:space-between;margin-top:40px}
.lot{width:250px}
.lot-photo{height:216px}
.lot h3{margin-top:14px;font-size:13px;font-weight:700;color:var(--ink);line-height:1.4;text-transform:uppercase}

.events{padding:30px 80px 0;height:540px}
.events .section-head{text-align:left}
.event-grid{display:grid;grid-template-columns:1fr 1fr;column-gap:60px;row-gap:40px;margin-top:36px}
.event{display:flex;gap:24px}
.event-photo{position:relative;width:160px;height:120px;flex:none}
.event-date{position:absolute;left:0;top:0;width:52px;height:56px;background:var(--red);color:var(--white);text-align:center;font-weight:700;font-size:22px;line-height:1.1;padding-top:6px}
.event-date small{display:block;font-size:12px;font-weight:600}
.event h3{font-size:17px;font-weight:700;color:var(--ink);text-transform:uppercase;margin-top:4px}
.event p{font-size:13px;line-height:1.6;margin:8px 0}
.event a{color:var(--red);font-size:13px;font-weight:600}

.site-footer{background:var(--footer);height:268px;padding:40px 80px 0;display:flex;gap:110px;color:var(--footer-text);font-size:13px}
.site-footer h4{color:var(--white);font-size:18px;font-weight:700;text-transform:uppercase;margin-bottom:20px}
.footer-nav li{list-style:none;line-height:1.75}
.tweet{display:flex;gap:12px;margin-bottom:18px;width:440px}
.tweet-dot{width:22px;height:22px;border-radius:50%;background:#4aa3df;flex:none}
.tweet p{line-height:1.55}
.tweet .handle{color:#4aa3df}
.footer-contact p{line-height:1.75}
.footer-contact strong{color:var(--white)}

.bottom-bar{height:48px;background:var(--red);color:var(--white);display:flex;align-items:center;justify-content:space-between;padding:0 80px;font-size:12px}
.socials{display:flex;gap:8px}
.socials i{width:24px;height:24px;border-radius:50%;background:var(--white)}
</style>
</head>
<body>

<header class="site-header">
  <a class="brand" href="#"><span class="brand-mark"></span>Tremaux Auctions</a>
  <div class="header-right">
    <div class="contact-line">
      <span class="phone-icon"><svg width="18" height="18" viewBox="0 0 24 24"><path fill="#c8102e" d="M6.6 10.8a15.1 15.1 0 006.6 6.6l2.2-2.2a1 1 0 011-.25 11.4 11.4 0 003.6.57 1 1 0 011 1V20a1 1 0 01-1 1A17 17 0 013 4a1 1 0 011-1h3.5a1 1 0 011 1c0 1.25.2 2.45.57 3.57a1 1 0 01-.25 1z"/></svg></span>
      <div><strong>800-555-0148</strong><span>info@tremauxauctions.com</span></div>
    </div>
    <a class="btn" href="#">Signup</a>
  </div>
</header>

<nav class="main-nav">
  <a href="#">Home</a><a href="#">About us</a><a href="#">Previous sales</a><a href="#">Next sales</a><a href="#">Contact</a><a href="#">How to buy</a><a href="#">Meet our specialists</a>
</nav>

<section class="hero">
  <div class="hero-photo" role="img" aria-label="Black and white photograph of a featured art piece with an ornate jewelled headdress"></div>
  <div class="hero-badge">
    <h1><span class="big">A Specialty</span><br>Auctions site<br>of finest arts</h1>
    <span class="shop">SHOP NOW</span>
    <span class="shop-arrow"></span>
  </div>
  <div class="hero-dots"><i></i><i class="on"></i><i></i><i></i></div>
</section>

<section class="welcome">
  <div class="welcome-photo" role="img" aria-label="Photograph of antique ceramics and glassware displayed at an auction preview"></div>
  <div class="welcome-text">
    <h2>Welcome to <strong>Tremaux Auctions</strong></h2>
    <p>Lorem ipsum dolor sit amet, consectetur adipiscing elit. Curabitur eget tincidunt nisi. Maecenas consectetur ante non nisl volutpat, vel finibus libero elementum. Sed at auctor velit. Proin vitae lectus nibh. Nunc ultricies ipsum justo. Phasellus tempor libero ipsum, sit amet facilisis lectus lobortis facilisis. Nunc ultricies ipsum justo. Phasellus tempor libero ipsum, sit amet facilisis lectus lobortis facilisis.</p>
    <a class="btn" href="#">Read more</a>
  </div>
</section>

<section class="on-sale">
  <h2 class="section-head">On Sales<span class="arrows"><i></i><i></i></span></h2>
  <div class="lots">
    <div class="lot"><div class="lot-photo" role="img" aria-label="Photograph of antique glass and ceramic objects" style="background:linear-gradient(135deg,#5a4a3a,#b79c72)"></div><h3>Vivamus a convallis sapien, sed congue quam</h3></div>
    <div class="lot"><div class="lot-photo" role="img" aria-label="Photograph of a red carnival mask with feathers" style="background:linear-gradient(135deg,#7a1018,#d8453a 55%,#e6c27a)"></div><h3>Malesuada nibh et tincidunt quam</h3></div>
    <div class="lot"><div class="lot-photo" role="img" aria-label="Photograph of ornate lanterns in a market" style="background:linear-gradient(135deg,#3a2a1a,#c07a30 55%,#e8c070)"></div><h3>Pellentesque laoreet turpis nec ipsum</h3></div>
    <div class="lot"><div class="lot-photo" role="img" aria-label="Photograph of hanging decorative lamps" style="background:linear-gradient(135deg,#2a1e16,#9a6a3a 55%,#d9b070)"></div><h3>Integer sodales diam eget nisl ultricies</h3></div>
  </div>
</section>

<section class="events">
  <h2 class="section-head">Upcoming Events</h2>
  <div class="event-grid">
    <article class="event"><div class="event-photo" role="img" aria-label="Photograph of an antique bronze piece" style="background:linear-gradient(135deg,#3a2a20,#9a6a40)"><span class="event-date">14<small>DEC</small></span></div><div><h3>Lorem ipsum is simply dummy text</h3><p>Lorem ipsum is simply dummy text of the printing and typesetting industry. Lorem ipsum has been.</p><a href="#">Read More &rarr;</a></div></article>
    <article class="event"><div class="event-photo" role="img" aria-label="Photograph of a red lacquered antique object" style="background:linear-gradient(135deg,#5a0a12,#b8303a)"><span class="event-date">21<small>DEC</small></span></div><div><h3>Lorem ipsum is simply dummy text</h3><p>Lorem ipsum is simply dummy text of the printing and typesetting industry. Lorem ipsum has been.</p><a href="#">Read More &rarr;</a></div></article>
    <article class="event"><div class="event-photo" role="img" aria-label="Photograph of candles and gilded decor" style="background:linear-gradient(135deg,#2a1a10,#c08a40)"><span class="event-date">07<small>JAN</small></span></div><div><h3>Lorem ipsum is simply dummy text</h3><p>Lorem ipsum is simply dummy text of the printing and typesetting industry. Lorem ipsum has been.</p><a href="#">Read More &rarr;</a></div></article>
    <article class="event"><div class="event-photo" role="img" aria-label="Photograph of a golden horse sculpture" style="background:linear-gradient(135deg,#1e140c,#b8842e)"><span class="event-date">18<small>JAN</small></span></div><div><h3>Lorem ipsum is simply dummy text</h3><p>Lorem ipsum is simply dummy text of the printing and typesetting industry. Lorem ipsum has been.</p><a href="#">Read More &rarr;</a></div></article>
  </div>
</section>

<footer class="site-footer">
  <div>
    <h4>Navigation</h4>
    <ul class="footer-nav"><li>About us</li><li>Previous sales</li><li>Next sales</li><li>Contact</li><li>How to buy</li><li>Meet our specialists</li></ul>
  </div>
  <div>
    <h4>Recent Tweets</h4>
    <div class="tweet"><span class="tweet-dot"></span><p><span class="handle">@tremauxauctions</span><br>Lorem ipsum is simply dummy text of the printing and typesetting industry. Lorem ipsum dolor.</p></div>
    <div class="tweet"><span class="tweet-dot"></span><p><span class="handle">@tremauxauctions</span><br>Lorem ipsum is simply dummy text of the printing and typesetting industry. Lorem ipsum dolor.</p></div>
  </div>
  <div class="footer-contact">
    <h4>Contact Us</h4>
    <p><strong>Tremaux Auctions</strong><br>2205 Elm Row St.<br>Calvera, CA 90412<br><br>Phone: 800-555-0148<br>Fax: 800-555-0149<br>Email: info@tremauxauctions.com</p>
  </div>
</footer>

<div class="bottom-bar">
  <span>tremauxauctions.com &copy; 2015 All Rights Reserved</span>
  <div class="socials"><i></i><i></i><i></i><i></i><i></i><i></i></div>
</div>

</body>
</html>
```